Restaurant Posters

Looking for two posters to be created for restaurant promos - see below for details:

Design #1 -
Want to highlight two main specials we offer - first is Tuesday BOGO Burgers (with purchase of two beverages), second is on Wednesday's we offer $0.75 Wings (includes traditional and boneless) and $2 off IPA's

Then at the bottom smaller would like to call out two less important offers - first is $2 off Nebraska Beers on Mondays, and the second is 1/2 off 19.2oz Crowlers on Thursdays

Design #2 -
Looking to create a sign up for our e-club and receive a free appetizer upon sign up, free burger on your birthday week, and access to exclusive deals and email offers

See attached for supporting docs you may use - don't have to but feel free to get creative with these. Would like the designs to be simple, and follow our brand look and feel as much as possible. Our website is not a good indication of our brand - I would go more off of our logos, and our menu design.

Need extra days to review

```html
<!DOCTYPE html>
<html lang="en">
<head>
<meta charset="utf-8">
<title>E-Club Sign Up</title>
<link rel="stylesheet" href="https://fonts.googleapis.com/css2?family=Barlow+Condensed:wght@400;500;600;700&family=Roboto+Slab:wght@400;700&family=Montserrat:wght@800&display=swap">
<style>
  :root {
    --page-bg: #f8f8f8;
    --brand-red: #d91a35;
    --white: #ffffff;
    --ink: #1b1b1b;
    --hint: #9a9a9a;
    --field-border: #9c9c9c;
  }
  * { box-sizing: border-box; margin: 0; padding: 0; }
  html, body { width: 1200px; height: 1200px; overflow: hidden; background: var(--page-bg); }
  body { position: relative; font-family: "Barlow Condensed", sans-serif; }

  .signup-card {
    position: absolute; left: 177px; top: 488px; width: 884px; height: 288px;
    background: var(--white);
    box-shadow: 0 6px 14px rgba(0,0,0,0.12);
  }
  .signup-card__pointer { position: absolute; left: 637px; top: -38px; width: 69px; height: 39px; }

  .promo {
    position: absolute; left: 0; top: 0; width: 517px; height: 288px;
    background: var(--brand-red); color: var(--white); text-align: center;
  }
  .promo__rule {
    position: absolute; left: 16px; width: 481px;
    border-top: 1px dashed rgba(255,255,255,0.55);
  }
  .promo__rule--top { top: 14px; }
  .promo__rule--bottom { top: 278px; }
  .promo__line { position: absolute; left: 0; width: 517px; white-space: nowrap; line-height: 1; }
  .promo__title { top: 22px; font-weight: 700; font-size: 80px; letter-spacing: 1px; padding-left: 2px; }
  .promo__offer { top: 98px; font-weight: 400; font-size: 34px; letter-spacing: 0.5px; }
  .promo__offer strong { font-weight: 700; }
  .promo__birthday { top: 138px; font-family: "Roboto Slab", serif; font-size: 20.5px; font-weight: 400; }
  .promo__birthday strong { font-weight: 700; }
  .promo__discounts { top: 178px; font-weight: 700; font-size: 42px; letter-spacing: 3px; }
  .promo__year { top: 224px; font-family: "Montserrat", sans-serif; font-weight: 800; font-size: 26px; letter-spacing: 5px; }

  .field {
    position: absolute; border: 1px solid var(--field-border); background: var(--white);
  }
  .field__label { position: absolute; left: 9px; top: 6px; font-size: 10.5px; font-weight: 500; color: var(--ink); }
  .field__hint { position: absolute; left: 9px; top: 22px; font-size: 12px; color: var(--hint); }
  .field--first { left: 541px; top: 50px; width: 155px; height: 43px; }
  .field--last { left: 704px; top: 50px; width: 156px; height: 43px; }
  .field--email { left: 541px; top: 103px; width: 319px; height: 43px; }

  .birthday-label { position: absolute; left: 549px; top: 164px; font-size: 10.5px; font-weight: 500; color: var(--ink); }
  .field--date { left: 590px; top: 156px; width: 99px; height: 27px; }
  .field--date .field__hint { top: 7px; left: 15px; word-spacing: 2px; }
  .field--date .slash { color: var(--ink); }
  .field--location { left: 703px; top: 156px; width: 126px; height: 27px; }
  .field--location .field__label { top: 7px; left: 13px; font-size: 11px; }
  .field__caret { position: absolute; right: 9px; top: 9px; width: 8px; height: 8px; }

  .submit-button {
    position: absolute; left: 633px; top: 201px; width: 132px; height: 30px;
    background: var(--brand-red); color: var(--white); border: none;
    font-family: "Barlow Condensed", sans-serif; font-weight: 600; font-size: 17px; line-height: 30px; text-align: center;
  }
  .fine-print {
    position: absolute; left: 580px; top: 244px; width: 240px; text-align: center;
    font-size: 6.6px; line-height: 9px; color: var(--ink); font-weight: 500;
  }
</style>
</head>
<body>
  <section class="signup-card">
    <svg class="signup-card__pointer" viewBox="0 0 69 39" aria-hidden="true">
      <polygon points="0,39 34.5,0 69,39" fill="#ffffff"/>
    </svg>

    <div class="promo">
      <div class="promo__rule promo__rule--top"></div>
      <h1 class="promo__line promo__title">JOIN OUR E-CLUB</h1>
      <p class="promo__line promo__offer">TO GET A <strong>FREE APPETIZER</strong></p>
      <p class="promo__line promo__birthday">and a <strong>free burger</strong> on your <strong>Birthday week!</strong></p>
      <p class="promo__line promo__discounts">ENJOY DISCOUNTS</p>
      <p class="promo__line promo__year">ALL YEAR LONG</p>
      <div class="promo__rule promo__rule--bottom"></div>
    </div>

    <div class="field field--first"><span class="field__label">First Name*</span><span class="field__hint">Sunny</span></div>
    <div class="field field--last"><span class="field__label">Last Name*</span><span class="field__hint">Parker</span></div>
    <div class="field field--email"><span class="field__label">Email*</span><span class="field__hint">yourself@mailnest.test</span></div>

    <span class="birthday-label">Birthday*</span>
    <div class="field field--date"><span class="field__hint">mm <span class="slash">/</span> dd <span class="slash">/</span> yyyy</span></div>
    <div class="field field--location">
      <span class="field__label">Favourite Location</span>
      <svg class="field__caret" viewBox="0 0 8 8" aria-hidden="true">
        <circle cx="4" cy="4" r="4" fill="#1b1b1b"/>
        <polyline points="2.2,3.2 4,4.9 5.8,3.2" fill="none" stroke="#ffffff" stroke-width="1.1"/>
      </svg>
    </div>

    <div class="submit-button">SIGN ME UP!</div>
    <p class="fine-print">*(All fields required) Must be 21 years of age. Some restrictions apply.<br>Must sign up 10 prior to your birthday to receive offer.</p>
  </section>
</body>
</html>
```